Wordpress Design Project - Wedding Magazine Website

After looking at a few similar websites I formed a layout and colour scheme design in my head.
Then I came across this site (www.plumeria-bells.co.uk) which very close to what I am looking for in terms of layout of the page content and colours. So I would like something very similar but not so similar it just looks like a clone of this site. Almost identical in terms of how the content is laid out but colours and look and feel can be changed.
I have also provided a sketch of how I would like the content of the page to flow. See attachment.
Similar websites: in terms of content, style and layout.
http://www.lacegarlandmag.com/ (the colour scheme is good on this site. I also would like a similar background image as they have on their site.)
http://www.velotrina.com/ (style and colour scheme is good on this site.)
of course you have the other sites i have reference in the initial tender.
Other general examples of wedding magazine style websites.
http://www.veilworks.co.uk/
http://www.thedayofpetals.co.uk/
http://www.silverringhour.com/
http://www.lovelark.com/
Style and layout: Wedding Theme
Colour Scheme: Clean and simple. White background in content area. Hints or highlights of grey/sliver, maybe pink here and there.
The page will flow as follows
Header part of the Page
- Name of the site on top left part of the page. “Wedvows Iberia”.
- 728x90 horizontal banner aligned on right.
- Under the site name “Wedvows Iberia” and banner will be a horizontal menu bar running the full width of the content
Main Content Area
- The main content column will be about 630px and the right sidebar will be about 330px. Similar width to most of the example URLs I have provided.
- Aligned to the left will be a slider
- Graphic or Pic: Guide to marrying in Spain: Everything you need to plan your wedding in spain.
- Graphic: Local Vendors Directory
- Articles 1 – 4
Right Sidebar (About 330px):
- Popular Post: Title of the Post and the first 2-3 lines of the post.
- 300x250 Ad Slot
- Locations: Title such as Barcelona then the first 2-3 lines of the post.
note: I haven't included a search box and login/register bits of content. i will leave it to you to figure out where these things will fit best on the page
=========================================================
Content of page
The horizontal menu bar: Home, Spanish Wedding Guide, Local Vendors Directory, Venues, Stag & Hen, Planning, Deals, Wedding Store.
For the wordpress theme the horizontal menubar will need to be a drop down menubar as we will have sub-menus for some of pages.
Images for slider
- Featured Venues
- Local vendors
- Deals
THE 2 COLUMN CONTENT AREA (Articles/Posts)
I am thinking that the first two bits of content in the 2 column area maybe should be graphics.
Spanish Wedding Guide -
Everything you need to plan your wedding in Spain.
Local Vendors Directory
(maybe this could be a graphic of a map of Spain)
=== from here you could use pictures or a mix of graphics and pictures to accompany each of these articles===
Front Page Main Content Articles
1. Legalities -
Want to tie the knot in Spain then you will find this post very useful.
2. Destination Barcelona -
Everything We LOVE About Barcelona!
3. Celebrity Weddings in Spain -
Find out who the latest celebrities to get married and Spain are and their chosen location.
4. Beach Weddings - With 4,964 km of coastline in Spain it is no surprise beach weddings are a popular choice.
under this will be the footer
Content we can populate later.
http://www.veilworks.co.uk/
http://www.lovelark.com/
Header part of the Page
- Under the site name “Wedvows Iberia” will be a horizontal menu bar running the full width of the content
Main Content Area
- The main content column will be about 630px and the right sidebar will be about 330px. Similar width to most of the
example URLs I have provided.
Graphic or Pic: Guide to marrying in Spain: Everything you need to plan your wedding in spain.
Article 1 – 4
- 300x250 Ad Slot
note: i have left out a search bar and login area. I will leave that up to you. where you think they will fit on the page.
Content of page
Images for slider
- Featured Venues
- Local vendors
- Deals
Spanish Wedding Guide -
Local Vendors Directory
1. Legalities -
Please contact me for any questions. it maybe better to speak via chatterlink or something.
Updates
Project Deadline Extended
Reason: It took me a few days to get acquainted with this site. As I don't have any designs in just yet I am extending the project a few days in order to give people time to submit their designs.
Something I would like to ad that i think designers will find useful.
The core of this site is the “Spanish Wedding Guide” and the “Local Vendor Directory”. These two things are what the site is all about so they need to feature. The viewers eyes must be drawn immediately to these two bit of information upon loading the page. These two things go underneath the slider.

```html
<!DOCTYPE html>
<html lang="en">
<head>
<meta charset="utf-8">
<title>Wedvows Iberia — Weddings with Sophistication</title>
<link href="https://fonts.googleapis.com/css2?family=Arimo:ital,wght@0,400;0,700;1,700&family=Cinzel:wght@400&family=Cormorant+Garamond:wght@400&display=swap" rel="stylesheet">
<style>
:root{
  --plum:#5b0b33;
  --plum-band:#a48fb6;
  --violet:#9a5fb5;
  --link:#a35fbd;
  --bronze:#a97b66;
  --slate:#6f6f6f;
  --text:#555;
  --copy:#4a4a4a;
  --page:#ebebeb;
  --panel:#e2e2e2;
  --line:#d6d6d6;
  --white:#fff;
  --gold-a:#8a4a1e;
  --gold-b:#d9a956;
  --magenta:#c23a9c;
}
*{box-sizing:border-box;margin:0;padding:0}
html,body{width:911px;height:1200px;overflow:hidden}
body{position:relative;background:var(--page);font-family:Arimo,Arial,sans-serif;color:var(--text)}
h1,h2,h3{font-weight:400}
.abs{position:absolute}
ul{list-style:none}

.top-band{left:0;top:0;width:911px;height:7px;background:var(--plum-band)}
.brand{left:0;top:7px;width:241px;height:75px;background:var(--white)}
.brand-mark{left:30px;top:23px;width:30px;height:30px;border-radius:50%;background:#e79fc6}
.brand-name{left:84px;top:14px;font-family:Cinzel,serif;color:var(--plum);font-size:24px;line-height:27px}
.banner{left:242px;top:7px;width:669px;height:75px;background:linear-gradient(90deg,var(--gold-a),#b87a3a 30%,var(--gold-b) 65%,#c79547)}
.banner-tag{right:52px;top:34px;font-family:Cinzel,serif;color:var(--white);font-size:15px;letter-spacing:1.5px}

.main-nav{left:7px;top:82px;width:897px;height:28px;background:var(--plum);border-top:1px solid #8c5474;display:flex;align-items:center;justify-content:space-between;padding:0 26px 0 21px;color:var(--white);font-size:10.5px;font-weight:700;letter-spacing:.5px}

.slider{left:30px;top:122px;width:542px;height:312px;background:linear-gradient(90deg,#e2dc3e,#f0eede 45%,#dcd447)}
.slider-arrow{top:236px;width:24px;height:50px;background:#e4e4ee;border:1px solid #b9b6cc}
.slider-arrow.prev{left:9px;border-radius:25px 0 0 25px}
.slider-arrow.next{left:572px;border-radius:0 25px 25px 0;background:#d7d0ee}

.popular{left:604px;top:122px;width:300px;height:312px;background:var(--panel)}
.panel-title{font-family:Cinzel,serif;color:var(--plum);font-size:17px;font-weight:400}
.popular .panel-title{left:16px;top:10px}
.popular-lead{left:14px;top:46px;font-style:italic;font-weight:700;font-size:12.5px;color:var(--copy)}
.popular-text{left:14px;width:274px;font-size:9.8px;line-height:12.2px;color:var(--copy)}
.btn{display:flex;align-items:center;justify-content:center;color:var(--white);font-size:10.5px;font-weight:700;border-radius:10px;letter-spacing:.3px}
.btn-bronze{background:var(--bronze);border:1px solid #8a5e4c}
.btn-slate{background:var(--slate)}
.popular .read-more{left:191px;top:244px;width:103px;height:19px}
.view-all{left:16px;top:290px;font-size:10.5px;font-weight:700;color:var(--link)}
.post-msg{left:172px;top:290px;font-size:10.5px;font-weight:700;color:var(--plum)}

.content{left:0;top:438px;width:597px;height:600px;background:var(--white)}
.guide-box{top:447px;height:171px;background:linear-gradient(#fff,#e5e5e5);border:1px solid #e0e0e0}
.guide-box .box-title{position:absolute;left:15px;top:7px;font-family:Cinzel,serif;font-size:16px;font-weight:400;color:var(--text)}
.guide-box ul{position:absolute;left:16px;top:37px}
.guide-box li{display:flex;align-items:center;height:22px;font-size:11px;color:#7a7a7a}
.guide-box li::before{content:"›";display:inline-flex;justify-content:center;align-items:center;width:15px;height:15px;background:var(--violet);color:#fff;font-size:12px;margin-right:9px;line-height:1}

.divider-v{left:291px;top:653px;width:1px;height:382px;background:var(--line)}
.divider-h{left:15px;top:821px;width:575px;height:1px;background:var(--line)}
.product{width:262px;height:130px}
.product-title{left:0;top:0;font-size:13px;font-weight:400;color:var(--text)}
.product-photo{left:-1px;top:25px;width:106px;height:70px;background:linear-gradient(#7a5a36,#b68a52);border:4px solid #dcdcdc}
.product-text{left:117px;top:25px;width:140px;font-size:10px;line-height:17px;color:var(--copy)}
.price{left:117px;top:65px;font-family:"Cormorant Garamond",serif;font-size:23px;color:var(--violet)}
.was{left:206px;top:76px;font-size:10.5px;color:var(--copy);text-decoration:line-through}
.product .btn{top:113px;width:103px;height:19px}
.product .add{left:-1px}
.product .details{left:154px}

.ad{left:618px;top:459px;width:273px;height:228px;background:linear-gradient(160deg,#e8c6cf,#f4eef0 45%,#a7b48f)}
.ad-click{left:158px;top:14px;width:110px;height:33px;background:#d99e6d;border-radius:8px;color:#fff;font-size:14px;display:flex;align-items:center;justify-content:center;letter-spacing:.5px}
.ad-title{left:14px;top:180px;font-family:Arimo,Arial,sans-serif;font-weight:400;color:var(--plum);font-size:22px;line-height:26px;letter-spacing:1px}

.locations{left:618px;top:699px;width:275px;height:315px;background:var(--white);border:1px solid #cfcfcf}
.locations .panel-title{left:9px;top:4px;color:var(--text);font-size:16px}
.loc-links{left:5px;top:45px;width:265px;font-size:10.5px;line-height:16.5px;color:var(--link)}
.map{left:10px;top:122px;width:252px;height:182px;background:linear-gradient(135deg,#d9d3a3,#e6df8e 50%,#cfcab4)}

.footer{left:0;top:1038px;width:911px;height:162px;background:#e5e5e5}
.foot-col{top:19px}
.foot-col h3{font-family:Cinzel,serif;font-weight:400;font-size:13px;color:var(--plum);line-height:16px;margin-bottom:10px}
.foot-col li{font-size:10px;color:var(--link);line-height:12px;padding-left:13px;letter-spacing:.3px}
.email{left:598px;top:57px;width:133px;height:21px;background:#fff;border:1px solid #888;font-size:10px;color:#999;padding:4px 5px}
.submit{left:665px;top:84px;width:66px;height:19px;background:linear-gradient(#e35bbf,var(--magenta));border:1px solid #8a2070;color:#fff;font-size:10px;font-weight:700;display:flex;align-items:center;justify-content:center}
.social{top:57px;width:22px;height:23px;border-radius:3px}
.pay{top:95px;height:13px;border-radius:2px}
.copyright{right:7px;top:142px;font-size:10.5px;color:var(--plum)}
</style>
</head>
<body>
<header>
  <div class="abs top-band"></div>
  <div class="abs brand">
    <div class="abs brand-mark"></div>
    <div class="abs brand-name">WEDVOWS<br>IBERIA</div>
  </div>
  <div class="abs banner" role="img" aria-label="Banner photo of two gold wedding rings on a warm gold background">
    <div class="abs banner-tag">WEDDINGS WITH SOPHISTICATION</div>
  </div>
  <nav class="abs main-nav">
    <span>HOME</span><span>|</span><span>SPANISH WEDDING GUIDE</span><span>|</span><span>LOCAL VENDORS DIRECTORY</span><span>|</span><span>VENUES, STAG &amp; HEN</span><span>|</span><span>PLANNING</span><span>|</span><span>DEALS</span><span>|</span><span>WEDDING STORE</span>
  </nav>
</header>

<div class="abs slider" role="img" aria-label="Slider photo of a bride and two bridesmaids in yellow dresses holding tulip bouquets"></div>
<div class="abs slider-arrow prev"></div>
<div class="abs slider-arrow next"></div>

<aside class="abs popular">
  <h2 class="abs panel-title">POPULAR POSTS</h2>
  <p class="abs popular-lead">Our Latest Wedding Collections are in</p>
  <p class="abs popular-text" style="top:75px">Lorem ipsum dolor sit amet, consectetuer adipiscing elit, sed diam nonummy nibh euismod tincidunt ut laoreet dolore magna aliquam erat volutpat. Ut wisi enim ad minim veniam, quis nostrud exerci tation ullamcorper suscipit lobortis nisl ut aliquip ex ea commodo consequat.</p>
  <p class="abs popular-text" style="top:148px">Lorem ipsum dolor sit amet, consectetuer adipiscing elit, sed diam nonummy nibh euismod tincidunt ut laoreet dolore magna aliquam erat volutpat. Ut wisi enim ad minim veniam, quis nostrud exerci tation ullamcorper suscipit lobortis nisl ut aliquip ex ea commodo consequat.</p>
  <div class="abs btn btn-bronze read-more">READ MORE</div>
  <span class="abs view-all">VIEW ALL POSTS</span>
  <span class="abs post-msg">POST YOUR MESSAGE</span>
</aside>

<main class="abs content"></main>

<section class="abs guide-box" style="left:15px;width:277px">
  <h2 class="box-title">WEDDING GUIDE</h2>
  <ul><li>Avenue of the Location 1</li><li>Avenue of the Location 2</li><li>Avenue of the Location 3</li><li>Avenue of the Location 4</li><li>Avenue of the Location 5</li></ul>
</section>
<section class="abs guide-box" style="left:303px;width:285px">
  <h2 class="box-title" style="left:10px">DIRECTIONS</h2>
  <ul style="left:11px"><li>Avenue of the Location 1</li><li>Avenue of the Location 2</li><li>Avenue of the Location 3</li><li>Avenue of the Location 4</li><li>Avenue of the Location 5</li></ul>
</section>

<div class="abs divider-v"></div>
<div class="abs divider-h"></div>

<article class="abs product" style="left:20px;top:675px">
  <h3 class="abs product-title">FULL COLLECTION</h3>
  <div class="abs product-photo" role="img" aria-label="Photo of a bride riding a horse in a golden field"></div>
  <p class="abs product-text">Lorem ipsum dolor sit amet, consectetur adipiscing elit</p>
  <span class="abs price">$142.98</span><span class="abs was">$150.00</span>
  <div class="abs btn btn-slate add">ADD TO CART</div>
  <div class="abs btn btn-bronze details">DETAILS</div>
</article>
<article class="abs product" style="left:324px;top:679px">
  <h3 class="abs product-title">FULL COLLECTION</h3>
  <div class="abs product-photo" role="img" aria-label="Photo of a bride riding a horse in a golden field"></div>
  <p class="abs product-text">Lorem ipsum dolor sit amet, consectetur adipiscing elit</p>
  <span class="abs price">$142.98</span><span class="abs was">$150.00</span>
  <div class="abs btn btn-slate add">ADD TO CART</div>
  <div class="abs btn btn-bronze details">DETAILS</div>
</article>
<article class="abs product" style="left:20px;top:849px">
  <h3 class="abs product-title">FULL COLLECTION</h3>
  <div class="abs product-photo" role="img" aria-label="Photo of a bride riding a horse in a golden field"></div>
  <p class="abs product-text">Lorem ipsum dolor sit amet, consectetur adipiscing elit</p>
  <span class="abs price">$142.98</span><span class="abs was">$150.00</span>
  <div class="abs btn btn-slate add" style="top:118px">ADD TO CART</div>
  <div class="abs btn btn-bronze details" style="top:118px">DETAILS</div>
</article>
<article class="abs product" style="left:324px;top:853px">
  <h3 class="abs product-title">FULL COLLECTION</h3>
  <div class="abs product-photo" role="img" aria-label="Photo of a bride riding a horse in a golden field"></div>
  <p class="abs product-text">Lorem ipsum dolor sit amet, consectetur adipiscing elit</p>
  <span class="abs price">$142.98</span><span class="abs was">$150.00</span>
  <div class="abs btn btn-slate add" style="left:-3px;top:114px">ADD TO CART</div>
  <div class="abs btn btn-bronze details" style="left:151px;top:114px">DETAILS</div>
</article>

<div class="abs ad" role="img" aria-label="Advertisement photo of a bouquet of pink and white roses">
  <div class="abs ad-click">CLICK HERE</div>
  <div class="abs ad-title">LINDELL BRIDAL</div>
</div>

<aside class="abs locations">
  <h2 class="abs panel-title">LOCATIONS</h2>
  <p class="abs loc-links">Avenue of the Location 1 &nbsp;|&nbsp; Avenue of the Location 2<br>Avenue of the Location 3 &nbsp;|&nbsp; Avenue of the Location 4<br>Avenue of the Location 5</p>
  <div class="abs map" role="img" aria-label="Street map with red pins marking the wedding locations"></div>
</aside>

<footer class="abs footer">
  <div class="abs foot-col" style="left:20px"><h3>INFORMATION</h3><ul><li>Contact</li><li>Delivery</li><li>Legal Notice</li><li>Terms and conditions</li><li>About us</li></ul></div>
  <div class="abs foot-col" style="left:231px"><h3>OUR OFFERS</h3><ul><li>New products</li><li>Top sellers</li><li>Specials</li><li>Manufacturers</li><li>Suppliers</li></ul></div>
  <div class="abs foot-col" style="left:423px"><h3>YOUR ACCOUNT</h3><ul><li>Your Account</li><li>Personal information</li><li>Addresses</li><li>Discount</li><li>Order history</li></ul></div>
  <div class="abs foot-col" style="left:598px"><h3>SIGNUP FOR<br>NEWSLETTER</h3></div>
  <div class="abs email">Email</div>
  <div class="abs submit">SUBMIT</div>
  <div class="abs social" style="left:782px;background:#3b5ba0"></div>
  <div class="abs social" style="left:806px;background:#3aa2db"></div>
  <div class="abs social" style="left:830px;background:#e88a2a"></div>
  <div class="abs social" style="left:854px;background:#c8332b"></div>
  <div class="abs pay" style="left:784px;width:41px;background:#2b5fa6"></div>
  <div class="abs pay" style="left:829px;width:20px;background:#2a3f8f"></div>
  <div class="abs pay" style="left:853px;width:22px;background:#e08a26"></div>
  <p class="abs copyright">© 2012 Wedvows Iberia All rights reserved</p>
</footer>
</body>
</html>
```